Need a design for Office wall, Pull up banner and brochure.

Hi there, We are looking for a design for our Mission, Vision and Values. We need it for our wall design, our pull up banner, and for our brochure. Full instructions have been provided in the Instructions png file submitted. Please let me know.

Our brand colours are:

Brand colours:
#0070BA
#000A3F
#6D6E71

• FF Meta Georgian Book

```html
<!DOCTYPE html>
<html lang="en">
<head>
<meta charset="UTF-8">
<title>Our Vision, Mission and Value</title>
<link rel="stylesheet" href="https://fonts.googleapis.com/css2?family=Arimo:wght@400;700&display=swap">
<style>
  :root {
    --page-light: #ffffff;
    --page-edge: #e4e4e6;
    --vision-green: #128c14;
    --mission-orange: #d05a3a;
    --value-blue: #2f8ff5;
    --body-ink: #000000;
  }
  * { margin: 0; padding: 0; box-sizing: border-box; }
  html, body { width: 700px; height: 1200px; overflow: hidden; }
  body {
    position: relative;
    background: radial-gradient(ellipse at 50% 50%, var(--page-light) 55%, var(--page-edge) 100%);
    font-family: "Arimo", Arial, sans-serif;
    color: var(--body-ink);
  }
  .timeline-graphic { position: absolute; left: 0; top: 0; width: 700px; height: 1200px; }
  .statement { position: absolute; }
  .statement-title {
    font-weight: 700;
    font-size: 22px;
    line-height: 26px;
    letter-spacing: 0.2px;
    margin-bottom: 5px;
  }
  .statement-body {
    font-size: 14.6px;
    line-height: 15.4px;
  }
  .statement--vision { left: 420px; top: 194px; }
  .statement--vision .statement-title { color: var(--vision-green); word-spacing: 6px; }
  .statement--mission { left: 41px; top: 514px; }
  .statement--mission .statement-title { color: var(--mission-orange); }
  .statement--value { left: 438px; top: 773px; }
  .statement--value .statement-title { color: var(--value-blue); }
</style>
</head>
<body>
<svg class="timeline-graphic" viewBox="0 0 700 1200" aria-hidden="true">
  <defs>
    <linearGradient id="hub-blue" x1="0" y1="0" x2="1" y2="0">
      <stop offset="0" stop-color="#0000c8"/>
      <stop offset="0.5" stop-color="#0000e6"/>
      <stop offset="1" stop-color="#0008c4"/>
    </linearGradient>
    <linearGradient id="ring-vision" x1="0" y1="0" x2="1" y2="0">
      <stop offset="0" stop-color="#06c50e"/>
      <stop offset="0.35" stop-color="#128c14"/>
      <stop offset="1" stop-color="#128c14"/>
    </linearGradient>
    <linearGradient id="ring-mission" x1="0" y1="0" x2="1" y2="0">
      <stop offset="0" stop-color="#ff6400"/>
      <stop offset="0.45" stop-color="#d05a3a"/>
      <stop offset="1" stop-color="#d05a3a"/>
    </linearGradient>
    <linearGradient id="ring-value" x1="0" y1="0" x2="1" y2="0">
      <stop offset="0" stop-color="#00c4ff"/>
      <stop offset="0.5" stop-color="#2a9cff"/>
      <stop offset="1" stop-color="#3388f0"/>
    </linearGradient>
    <filter id="ring-shadow" x="-30%" y="-30%" width="160%" height="160%">
      <feGaussianBlur stdDeviation="6"/>
    </filter>
    <path id="star-shape" d="M0,-44 L11.8,-16.2 L41.8,-13.6 L19,6.2 L25.9,35.6 L0,20 L-25.9,35.6 L-19,6.2 L-41.8,-13.6 L-11.8,-16.2 Z"/>
  </defs>

  <!-- connecting necks -->
  <polygon points="295,440 365,400 385,455 318,495" fill="#0000e0"/>
  <polygon points="318,680 385,720 365,775 295,735" fill="#0000d8"/>
  <circle cx="305" cy="465" r="20" fill="#ffffff"/>
  <circle cx="371" cy="431" r="20" fill="#ffffff"/>
  <circle cx="305" cy="711" r="20" fill="#ffffff"/>
  <circle cx="371" cy="746" r="20" fill="#ffffff"/>

  <!-- hubs -->
  <g class="hub hub--vision">
    <circle cx="268" cy="309" r="140" fill="url(#hub-blue)"/>
    <circle cx="276" cy="324" r="108" fill="#000070" filter="url(#ring-shadow)"/>
    <circle cx="268" cy="309" r="107" fill="url(#ring-vision)"/>
    <circle cx="268" cy="309" r="81" fill="#ffffff"/>
    <circle cx="268" cy="309" r="40" fill="none" stroke="#000" stroke-width="4.5"/>
    <circle cx="268" cy="309" r="27" fill="#000"/>
    <circle cx="283" cy="294" r="15" fill="#ffffff"/>
  </g>

  <g class="hub hub--mission">
    <circle cx="407" cy="588" r="140" fill="url(#hub-blue)"/>
    <circle cx="415" cy="603" r="108" fill="#000070" filter="url(#ring-shadow)"/>
    <circle cx="407" cy="588" r="107" fill="url(#ring-mission)"/>
    <circle cx="407" cy="588" r="81" fill="#ffffff"/>
    <circle cx="406" cy="589" r="40" fill="none" stroke="#000" stroke-width="4.5"/>
    <circle cx="406" cy="589" r="21" fill="none" stroke="#000" stroke-width="4.5"/>
    <line x1="408" y1="587" x2="452" y2="543" stroke="#ffffff" stroke-width="12"/>
    <line x1="406" y1="589" x2="437" y2="558" stroke="#000" stroke-width="4.5" stroke-linecap="round"/>
    <polygon points="428,558 441,545 444,544 447,550 452,552 439,566 434,564 430,562" fill="#000"/>
  </g>

  <g class="hub hub--value">
    <circle cx="268" cy="868" r="140" fill="url(#hub-blue)"/>
    <circle cx="276" cy="883" r="108" fill="#000070" filter="url(#ring-shadow)"/>
    <circle cx="268" cy="868" r="107" fill="url(#ring-value)"/>
    <circle cx="268" cy="868" r="81" fill="#ffffff"/>
    <use href="#star-shape" transform="translate(268,872)" fill="none" stroke="#000" stroke-width="4.5" stroke-linejoin="round"/>
    <use href="#star-shape" transform="translate(268,874) scale(0.42)" fill="#000"/>
  </g>
</svg>

<section class="statement statement--vision">
  <h2 class="statement-title">OUR VISION</h2>
  <p class="statement-body">Lorem ipsum dolor sit amet.<br>Dolores sit lorem. Eirmod<br>feugait dolore facilisi imperdiet<br>et justo. Sit dolore sed dolor.<br>Vulputate aliquyam iriure dolor<br>duo kasd est. Sit molestie<br>vulputate. Ea eirmod ipsum<br>kasd qui et consetetur. Et te<br>dolor. Consetetur takimata clita<br>sea consetetur duo.</p>
</section>

<section class="statement statement--mission">
  <h2 class="statement-title">OUR MISSION</h2>
  <p class="statement-body">Lorem ipsum dolor sit amet.<br>Dolores sit lorem. Eirmod<br>feugait dolore facilisi imperdiet<br>et justo. Sit dolore sed dolor.<br>Vulputate aliquyam iriure dolor<br>duo kasd est. Sit molestie<br>vulputate. Ea eirmod ipsum<br>kasd qui et consetetur. Et te<br>dolor. Consetetur takimata clita<br>sea consetetur duo.</p>
</section>

<section class="statement statement--value">
  <h2 class="statement-title">OUR VALUE</h2>
  <p class="statement-body">Lorem ipsum dolor sit amet.<br>Dolores sit lorem. Eirmod<br>feugait dolore facilisi imperdiet<br>et justo. Sit dolore sed dolor.<br>Vulputate aliquyam iriure dolor<br>duo kasd est. Sit molestie<br>vulputate. Ea eirmod ipsum<br>kasd qui et consetetur. Et te<br>dolor. Consetetur takimata clita<br>sea consetetur duo.<br>Duo lorem et est. Suscipit<br>hendrerit est stet eirmod. Stet<br>sit sadipscing nulla. Labore<br>dolor et consetetur. Consequat</p>
</section>
</body>
</html>
```